I need a luxury/high-end real estate looking website for my Vending business

Hello & thank you in advance for your time spent on this project.

I have a vending business (Copper Lantern Vending Services) based here in downtown Miami & my clients are high-end/luxury buildings throughout the area.
We offer free placement of 5 vending machine options (snacks, drinks, laundry products, healthy options or combo machine) to high traffic locations.

The goal of this website is to be a lead generator. So having an inquiry form on the top of the page is key.

Aesthetically, I want the website to feel like a high-end commercial real estate website. We service luxury buildings, so I want that look of the downtown skyline mixed in with the vending machine images throughout the site.

On the main page, it would be :
*the inquiry form (name of location, # of machines, machine option, contact info)
*What we do section - vending machine placement, bi-weekly or monthly refill service & ongoing customer support.
*5 vending machine options section - (with clickable images to see what all products you can have the machine filled with)
*reviews section
*social feed or blog post section
*about us section
then of course the contact info etc at the bottom of page

For the question ''how many pages do you need designed'', I answered 5+, which is in reference to the main page outlined above plus the 5 clickable images that takes you to the product options. I'm assuming the clickable images would be pages on their own.

Target Market(s)

High traffic businesses & residences in downtown Miami

Industry/Entity Type

Vending Machines

Coding

Coded - Design and coding required

Number of Pages Required

5+ page

Requirements
Must have
• Inquiry form
Nice to have
• To have a feel of a luxury/high-end commercial real estate website

```html
<!DOCTYPE html>
<html lang="en">
<head>
<meta charset="utf-8">
<title>Copper Lantern Vending Services</title>
<link href="https://fonts.googleapis.com/css2?family=Outfit:wght@300;400;500;600;700;800;900&display=swap" rel="stylesheet">
<style>
:root{
  --orange:#f4553b;
  --orange-dark:#e2452c;
  --ink:#1f2126;
  --dark:#25272c;
  --dark-2:#2c2e34;
  --grey-bg:#f1f1f1;
  --text:#6c6d72;
  --white:#ffffff;
}
*{margin:0;padding:0;box-sizing:border-box}
html,body{width:1200px;height:4048px;overflow:hidden}
body{font-family:"Outfit",sans-serif;color:var(--ink);background:var(--white);position:relative}
.abs{position:absolute}
.btn{position:absolute;display:flex;align-items:center;justify-content:center;background:var(--orange);color:var(--white);border-radius:18px;font-size:13px;font-weight:500}
p{color:var(--text);font-size:13px;line-height:1.75;font-weight:300}

/* hero */
.hero{position:absolute;left:0;top:0;width:1200px;height:620px;overflow:hidden}
.hero-photo{position:absolute;inset:0;background:radial-gradient(ellipse at 35% 40%,#6b5a4c 0%,#2e3138 45%,#15171c 100%)}
.hero-photo::after{content:"";position:absolute;inset:0;background:linear-gradient(90deg,rgba(10,20,40,.35),rgba(30,20,20,.55))}
.brand{position:absolute;left:110px;top:22px;color:var(--white);font-size:20px;font-weight:600;line-height:1.1;width:210px}
.nav{position:absolute;left:452px;top:28px;display:flex;gap:26px}
.nav a{color:var(--white);text-decoration:none;font-size:13px;font-weight:500;padding-bottom:6px}
.nav a.active{color:var(--orange);border-bottom:2px solid var(--orange)}
.hero-title{position:absolute;left:684px;top:262px;color:var(--white);font-size:46px;font-weight:600;line-height:1.13}

.inquiry{position:absolute;left:0;top:520px;width:600px;height:225px;background:var(--orange)}
.field{position:absolute;width:218px;border-bottom:1px solid rgba(255,255,255,.8);color:var(--white);font-size:12px;padding-bottom:8px;display:flex;justify-content:space-between}
.submit{position:absolute;left:232px;top:165px;width:122px;height:34px;background:var(--white);color:var(--orange);border-radius:17px;display:flex;align-items:center;justify-content:center;font-size:13px;font-weight:500}

.contact-bar{position:absolute;left:600px;top:620px;width:600px;height:125px;background:var(--dark-2);color:var(--white)}
.contact-item{position:absolute;top:30px}
.contact-item small{display:block;font-size:10px;color:#a9abb1;letter-spacing:1px;margin-left:34px}
.contact-item strong{display:block;font-size:17px;font-weight:500;margin-top:18px}

/* intro */
.sec-title{font-size:40px;font-weight:600;line-height:1.15;color:var(--ink)}
.sec-title span{color:var(--orange)}
.about-word{position:absolute;left:0;top:1120px;width:1200px;text-align:center;font-size:220px;font-weight:900;letter-spacing:4px;line-height:1;background:linear-gradient(90deg,#3b3e46,#b0543f,#5a6f8a,#2d3038,#c88a4a,#34373e);-webkit-background-clip:text;background-clip:text;color:transparent}

/* services */
.services{position:absolute;left:0;top:1390px;width:1200px;height:490px;background:var(--grey-bg)}
.svc{position:absolute;top:170px;width:210px}
.svc h3{font-size:20px;font-weight:600;line-height:1.2;margin-top:48px;margin-bottom:14px}

/* options */
.options-photo{position:absolute;left:0;top:1895px;width:600px;height:480px;background:linear-gradient(120deg,#1b3f7a 0%,#2c5ea8 30%,#b8332e 55%,#d5d8de 75%,#6d7380 100%)}
.opt-list{position:absolute;left:665px;top:2100px;list-style:none}
.opt-list li{display:flex;align-items:center;gap:16px;height:40px;font-size:13px;font-weight:400}

/* testimonials */
.quote-block{position:absolute;left:110px;top:2452px;width:52px;height:170px;background:var(--dark)}
.testi{position:absolute;top:2525px;width:365px}
.testi .by{display:flex;align-items:center;gap:14px;margin-top:28px;font-size:12px;color:var(--ink)}
.testi .by i{display:block;width:76px;height:1px;background:var(--ink)}
.arrow{position:absolute;left:1088px;width:20px;height:20px;border-radius:50%;background:#e7e7e9;display:flex;align-items:center;justify-content:center}

/* blog */
.blog-bg{position:absolute;left:0;top:2755px;width:770px;height:210px;background:var(--grey-bg)}
.card{position:absolute;top:2910px;width:312px;height:390px;overflow:hidden}
.card .shade{position:absolute;left:0;right:0;bottom:0;height:120px;background:linear-gradient(180deg,rgba(0,0,0,0),rgba(0,0,0,.85))}
.card .tag{position:absolute;left:18px;bottom:82px;background:var(--orange);color:var(--white);font-size:10px;padding:2px 8px}
.card h4{position:absolute;left:18px;bottom:40px;color:var(--white);font-size:19px;font-weight:500}
.card .meta{position:absolute;left:18px;bottom:14px;color:#d5d5d8;font-size:10px;display:flex;gap:22px}

/* gallery */
.gallery{position:absolute;left:0;top:3400px;width:1200px;height:215px;display:flex}
.gallery div{flex:1}
.play{position:absolute;left:428px;top:3480px;width:48px;height:48px;border-radius:50%;background:var(--orange);display:flex;align-items:center;justify-content:center}

/* footer */
.footer{position:absolute;left:0;top:3615px;width:1200px;height:433px;background:var(--dark);color:var(--white)}
.f-col{position:absolute;top:60px;font-size:12px;font-weight:300;line-height:1.95}
.f-row{display:flex;gap:14px;align-items:flex-start;margin-bottom:18px;line-height:1.6}
.newsletter{position:absolute;left:860px;top:60px;width:230px}
.newsletter .input{border-bottom:1px solid #6b6d73;color:#9a9ca2;font-size:11px;padding-bottom:8px;display:flex;justify-content:space-between}
.newsletter .btn{position:relative;width:110px;height:32px;margin-top:22px}
.footer-rule{position:absolute;left:110px;top:345px;width:980px;height:1px;background:#3b3d43}
.copyright{position:absolute;left:0;top:370px;width:1200px;text-align:center;font-size:11px;color:#c7c8cc}
.top-link{position:absolute;left:1160px;top:370px;font-size:10px;color:#c7c8cc}
</style>
</head>
<body>

<header class="hero">
  <div class="hero-photo" role="img" aria-label="Woman selecting from an illuminated vending machine at night"></div>
  <div class="brand">Copper Lantern Vending Services</div>
  <nav class="nav">
    <a class="active">Home</a><a>About</a><a>Services</a><a>Shop</a><a>Features</a><a>Contact</a>
  </nav>
  <div class="btn" style="left:932px;top:20px;width:108px;height:36px">Get Started</div>
  <h1 class="hero-title">Copper Lantern<br>Vending Services</h1>
  <div class="btn" style="left:684px;top:398px;width:100px;height:32px">Get Started</div>
</header>

<form class="inquiry">
  <div class="field" style="left:110px;top:30px">No.of machines <span>▾</span></div>
  <div class="field" style="left:322px;top:30px">Category <span>▾</span></div>
  <div class="field" style="left:110px;top:106px">Phone</div>
  <div class="field" style="left:322px;top:106px">Email</div>
  <div class="submit">Submit Now</div>
</form>

<section class="contact-bar">
  <div class="contact-item" style="left:38px">
    <svg class="abs" style="left:0;top:-2px" width="18" height="18" viewBox="0 0 24 24" fill="none" stroke="#f4553b" stroke-width="2"><path d="M22 16.9v3a2 2 0 0 1-2.2 2 19.8 19.8 0 0 1-8.6-3.1 19.5 19.5 0 0 1-6-6A19.8 19.8 0 0 1 2.1 4.2 2 2 0 0 1 4.1 2h3a2 2 0 0 1 2 1.7c.1.9.4 1.8.7 2.7a2 2 0 0 1-.5 2.1L8 9.8a16 16 0 0 0 6 6l1.3-1.3a2 2 0 0 1 2.1-.4c.9.3 1.8.6 2.7.7a2 2 0 0 1 1.7 2z"/></svg>
    <small>PHONE</small>
    <strong>+1 305 555 0142</strong>
  </div>
  <div class="contact-item" style="left:320px">
    <svg class="abs" style="left:0;top:-2px" width="18" height="18" viewBox="0 0 24 24" fill="none" stroke="#f4553b" stroke-width="2"><rect x="2" y="4" width="20" height="16" rx="2"/><path d="m22 6-10 7L2 6"/></svg>
    <small>EMAIL</small>
    <strong>hello@copperlantern.co</strong>
  </div>
</section>

<section class="intro">
  <h2 class="sec-title abs" style="left:110px;top:832px">Copper Lantern<br><span>Vending Services</span></h2>
  <div class="abs" style="left:525px;top:826px;width:565px">
    <p>Lorem ipsum dolor sit amet, consectetur adipiscing elit sed do eiusmod tempor incididunt ut labore et dolore magna aliqua. Ut enim ad minim veniam, quis nostrud exercitation ullamco laboris nisi ut aliquip ex ea commodo consequat. Duis aute irure dolor in reprehenderit in voluptate velit esse cillum dolore eu fugiat nulla pariatur.</p>
    <p style="margin-top:18px">Excepteur sint occaecat cupidatat non proident, sunt in culpa qui officia deserunt mollit anim id est laborum. Lorem ipsum dolor sit amet, consectetur adipiscing elit, sed do eiusmod tempor incididunt ut labore et dolore magna aliqua.</p>
  </div>
  <div class="btn" style="left:525px;top:1056px;width:108px;height:34px">Learn More</div>
  <div class="about-word" role="img" aria-label="About Us lettering filled with vending machine photography">ABOUT US</div>
</section>

<section class="services">
  <h2 class="sec-title abs" style="left:110px;top:100px">Our <span>Services</span></h2>
  <div class="btn" style="left:935px;top:100px;width:118px;height:36px">View More</div>

  <div class="svc" style="left:110px">
    <svg width="40" height="44" viewBox="0 0 40 44" fill="none" stroke="#f4553b" stroke-width="2"><rect x="6" y="2" width="28" height="40" rx="2"/><rect x="11" y="8" width="18" height="20"/><line x1="11" y1="34" x2="22" y2="34"/><circle cx="28" cy="34" r="2"/></svg>
    <h3>Duis aute irure do lor in repre</h3>
    <p>Lorem ipsum dolor sit amet, consec tetur adipiscing elit, sed do eiusmod tempor incididunt ut labore et dolore magna aliqua.</p>
  </div>
  <div class="svc" style="left:360px">
    <svg width="44" height="44" viewBox="0 0 44 44" fill="none" stroke="#f4553b" stroke-width="2"><rect x="4" y="4" width="36" height="36" rx="3"/><path d="M12 16h20M12 24h20M12 32h12"/></svg>
    <h3>Duis aute irure do lor in repre</h3>
    <p>Lorem ipsum dolor sit amet, consec tetur adipiscing elit, sed do eiusmod tempor incididunt ut labore et dolore magna aliqua.</p>
  </div>
  <div class="svc" style="left:610px">
    <svg width="44" height="44" viewBox="0 0 44 44" fill="none" stroke="#f4553b" stroke-width="2"><circle cx="22" cy="22" r="8"/><path d="M22 4v6M22 34v6M4 22h6M34 22h6M9 9l4 4M31 31l4 4M9 35l4-4M31 13l4-4"/></svg>
    <h3>Duis aute irure do lor in repre</h3>
    <p>Lorem ipsum dolor sit amet, consec tetur adipiscing elit, sed do eiusmod tempor incididunt ut labore et dolore magna aliqua.</p>
  </div>
  <div class="svc" style="left:860px">
    <svg width="44" height="44" viewBox="0 0 44 44" fill="none" stroke="#f4553b" stroke-width="2"><rect x="4" y="18" width="36" height="22" rx="2"/><path d="M10 18V10h24v8M16 26h12"/><circle cx="22" cy="6" r="3"/></svg>
    <h3>Duis aute irure do lor in repre</h3>
    <p>Lorem ipsum dolor sit amet, consec tetur adipiscing elit, sed do eiusmod tempor incididunt ut labore et dolore magna aliqua.</p>
  </div>
</section>

<section class="options">
  <div class="options-photo" role="img" aria-label="Row of brightly lit drink and snack vending machines"></div>
  <h2 class="sec-title abs" style="left:665px;top:1962px;font-size:36px;font-weight:500">Variety of Vending<br>Machine Options</h2>
  <ul class="opt-list">
    <li><svg width="22" height="22" viewBox="0 0 24 24" fill="none" stroke="#f4553b" stroke-width="1.8"><rect x="5" y="3" width="14" height="18" rx="2"/><path d="M9 8h6M9 12h6"/></svg>Snacks</li>
    <li><svg width="22" height="22" viewBox="0 0 24 24" fill="none" stroke="#f4553b" stroke-width="1.8"><path d="M6 4h12l-2 17H8z"/><path d="M7 9h10"/></svg>Drinks</li>
    <li><svg width="22" height="22" viewBox="0 0 24 24" fill="none" stroke="#f4553b" stroke-width="1.8"><rect x="4" y="2" width="16" height="20" rx="2"/><circle cx="12" cy="13" r="5"/></svg>Laundry products</li>
    <li><svg width="22" height="22" viewBox="0 0 24 24" fill="none" stroke="#f4553b" stroke-width="1.8"><path d="M12 21s-8-5-8-11a4.5 4.5 0 0 1 8-2.8A4.5 4.5 0 0 1 20 10c0 6-8 11-8 11z"/></svg>Healthy options</li>
  </ul>
</section>

<section class="testimonials">
  <div class="quote-block">
    <svg class="abs" style="left:8px;top:64px" width="36" height="30" viewBox="0 0 36 30" fill="#f4553b"><path d="M0 30V16C0 7 5 1 14 0v6c-5 1-7 4-7 9h7v15zM20 30V16c0-9 5-15 14-16v6c-5 1-7 4-7 9h7v15z"/></svg>
  </div>
  <h2 class="sec-title abs" style="left:235px;top:2440px">People <span>Says</span></h2>
  <div class="testi" style="left:235px">
    <p>Lorem ipsum dolor sit amet, consectetur adipiscing elit, sed do eiusmod tempor incididunt ut labore et dolore magna aliqua. Ut enim ad minim veniam, quis nostrud exercitation ullamco laboris nisi ut aliquip ex ea commodo consequat.</p>
    <div class="by"><i></i>Maria Alvarez</div>
  </div>
  <div class="testi" style="left:652px">
    <p>Lorem ipsum dolor sit amet, consectetur adipiscing elit, sed do eiusmod tempor incididunt ut labore et dolore magna aliqua. Ut enim ad minim veniam, quis nostrud exercitation ullamco laboris nisi ut aliquip ex ea commodo consequat.</p>
    <div class="by"><i></i>Maria Alvarez</div>
  </div>
  <div class="arrow" style="top:2538px"><svg width="8" height="8" viewBox="0 0 8 8"><path d="M2 1l3 3-3 3" stroke="#25272c" fill="none" stroke-width="1.4"/></svg></div>
  <div class="arrow" style="top:2585px"><svg width="8" height="8" viewBox="0 0 8 8"><path d="M2 1l3 3-3 3" stroke="#25272c" fill="none" stroke-width="1.4"/></svg></div>
</section>

<section class="blog">
  <div class="blog-bg"></div>
  <h2 class="sec-title abs" style="left:110px;top:2838px">Blog &amp; <span>News</span></h2>
  <article class="card" style="left:110px">
    <div class="abs" style="inset:0;background:linear-gradient(160deg,#3a3f52,#8a5a4a 55%,#1c1e24)" role="img" aria-label="Woman using a vending machine in a dim lobby"></div>
    <div class="shade"></div><span class="tag">News</span>
    <h4>Duis aute irure dolor</h4>
    <div class="meta"><span>Jan 02, 2022</span><span>05</span></div>
  </article>
  <article class="card" style="left:448px">
    <div class="abs" style="inset:0;background:linear-gradient(160deg,#2c3a66,#6a2d3c 50%,#1a1c22)" role="img" aria-label="Close view of a stocked snack vending machine"></div>
    <div class="shade"></div><span class="tag">News</span>
    <h4>Duis aute irure dolor</h4>
    <div class="meta"><span>Jan 02, 2022</span><span>05</span></div>
  </article>
  <article class="card" style="left:786px">
    <div class="abs" style="inset:0;background:linear-gradient(160deg,#c83a32,#7a2226 50%,#2a2c32)" role="img" aria-label="Red snack vending machine in a station"></div>
    <div class="shade"></div><span class="tag">News</span>
    <h4>Duis aute irure dolor</h4>
    <div class="meta"><span>Jan 02, 2022</span><span>05</span></div>
  </article>
</section>

<section>
  <div class="gallery">
    <div style="background:linear-gradient(180deg,#8fa0a8,#4d5a60)" role="img" aria-label="Vending machine in a bright corridor"></div>
    <div style="background:linear-gradient(180deg,#2b2d33,#1a1b20)" role="img" aria-label="Vending machines in a dark hall"></div>
    <div style="background:linear-gradient(120deg,#c8312c,#e8e4e0 60%,#b52a28)" role="img" aria-label="Red and white drink vending machines"></div>
    <div style="background:linear-gradient(120deg,#d8d4cf,#b9796b 60%,#8b3f3c)" role="img" aria-label="Woman choosing a drink from a vending machine"></div>
  </div>
  <div class="play"><svg width="16" height="16" viewBox="0 0 16 16" fill="none" stroke="#fff" stroke-width="1.6"><rect x="2" y="3" width="12" height="10" rx="2"/><path d="M7 6l3 2-3 2z" fill="#fff"/></svg></div>
</section>

<footer class="footer">
  <div class="f-col" style="left:110px;width:230px">
    <div class="f-row"><svg width="14" height="14" viewBox="0 0 24 24" fill="none" stroke="#f4553b" stroke-width="2"><path d="M12 22s-7-7-7-12a7 7 0 0 1 14 0c0 5-7 12-7 12z"/><circle cx="12" cy="10" r="2.5"/></svg><span>123, Lorem ipsum dolor sit amet, consectetur</span></div>
    <div class="f-row"><svg width="14" height="14" viewBox="0 0 24 24" fill="none" stroke="#f4553b" stroke-width="2"><path d="M22 16.9v3a2 2 0 0 1-2.2 2A19.8 19.8 0 0 1 2.1 4.2 2 2 0 0 1 4.1 2h3l2 5-2.5 2a16 16 0 0 0 7.5 7.5l2-2.5 5 2z"/></svg><span>+1 305 555 0142</span></div>
    <div class="f-row"><svg width="14" height="14" viewBox="0 0 24 24" fill="none" stroke="#f4553b" stroke-width="2"><rect x="2" y="4" width="20" height="16" rx="2"/><path d="m22 6-10 7L2 6"/></svg><span>hello@copperlantern.co</span></div>
  </div>
  <div class="f-col" style="left:472px">Home<br>About<br>Service<br>Blog<br>Reviews<br>Contact</div>
  <div class="f-col" style="left:664px">Privacy policy<br>Terms of service<br>Faq<br>About<br>Contact<br>Support</div>
  <div class="newsletter">
    <div class="input">Email address <svg width="12" height="12" viewBox="0 0 24 24" fill="none" stroke="#9a9ca2" stroke-width="2"><rect x="2" y="4" width="20" height="16" rx="2"/><path d="m22 6-10 7L2 6"/></svg></div>
    <div class="btn">Subscribe</div>
  </div>
  <div class="footer-rule"></div>
  <div class="copyright">© Copyright Copper Lantern 2022. All rights reserved</div>
  <div class="top-link">TOP</div>
</footer>

</body>
</html>
```